Baby Care Print Log for Nannies and Parents- Creating a brand/style I can use across different forms

I am creating a notebook for babysitters to use to communicate with parents about the children they care for. I will be creating many different forms (emergency contacts, daily logs, shopping lists, etc.)
I need a look and feel from which to style these forms from. I am starting by designing the daily baby care log. I need a designer to take my Word doc with just text on it, and create a visual approach to make this visually appealing.
I do not want this to be extremely "babyish" with cartoon styling. I want it to be more of a professional looking style. I would like to be able to color each different document a different color palette, yet keep the similar look and feel. My logo is attached for inspiration. I use real photography across my website quillharborpages.com.
Updates
I will be re-designing my Wordpress website based on what design I like best and also will need other forms completed once I pick a design. I am hoping to work with someone who I can hire for further development needs as well. Added Saturday, February 11, 2017
Target Market(s)
Professional Parents
Industry/Entity Type
Education
Requirements
Must have
- color, pop, visual appeal
- Please use the color in my logo and any complementary colors that you think work well with it. I definitely like colored patterns, ombre, colored backgrounds, etc. I'd prefer for it not to be completely white with only pops of color here and there.
Nice to have
- My logo somewhere subtly on the form
- Photography elements
Should not have
- cartoon images of babies, etc. I use real photography across my website with the exception of my logo umbrella.

```html
<!DOCTYPE html>
<html lang="en">
<head>
<meta charset="utf-8">
<title>Daily Care Log – Quill Harbor Pages</title>
<link rel="stylesheet" href="https://fonts.googleapis.com/css2?family=Comic+Neue:wght@400;700&display=swap">
<style>
  :root {
    --stage: #bfbfbf;
    --paper: #ffffff;
    --teal: #2a9fbb;
    --teal-deep: #33a5bf;
    --teal-light: #7fd0e2;
    --ink: #1d1d1d;
  }
  * { box-sizing: border-box; margin: 0; padding: 0; }
  html, body { width: 1200px; height: 1200px; overflow: hidden; }
  body {
    background: var(--stage);
    font-family: "Comic Neue", "Comic Sans MS", sans-serif;
    color: var(--teal);
    position: relative;
  }
  .log-page {
    position: absolute;
    left: 220px; top: 70px;
    width: 760px; height: 1060px;
    background: var(--paper);
    overflow: hidden;
    box-shadow: 0 6px 18px rgba(0,0,0,.25);
  }
  .abs { position: absolute; }
  .section-title { font-weight: 700; font-size: 17px; }
  .label { font-size: 15px; }
  .hero-photo {
    left: 325px; top: 28px; width: 110px; height: 130px;
    background: linear-gradient(180deg, #e9d2bf 0%, #cdb79c 55%, #f1f1f1 100%);
    border-radius: 6px;
  }
  .brand {
    left: 0; width: 760px; top: 165px; text-align: center;
    display: flex; justify-content: center; align-items: center; gap: 10px;
  }
  .brand-dot { width: 18px; height: 18px; border-radius: 50%; background: var(--teal); }
  .brand-name { font-weight: 700; font-size: 34px; color: var(--ink); }
  .field { display: flex; align-items: flex-end; gap: 6px; font-weight: 700; font-size: 16px; }
  .field .rule { border-bottom: 1.5px solid var(--teal); height: 16px; }
  .grid { border-collapse: collapse; font-size: 14px; }
  .grid td { border: 1.5px solid var(--teal); height: 27px; width: 45px; padding: 0 6px; }
  .grid td.head { width: 85px; }
  .box {
    display: inline-block; width: 21px; height: 21px;
    border: 1.5px solid var(--teal); vertical-align: middle;
  }
  .ring {
    display: inline-block; width: 17px; height: 17px; border-radius: 50%;
    border: 1.5px solid var(--teal); vertical-align: middle; margin-right: 8px;
  }
  .diaper-row { display: flex; align-items: center; gap: 18px; height: 38px; }
  .diaper-row .rule { width: 50px; border-bottom: 1.5px solid var(--teal); margin-right: 4px; align-self: flex-end; margin-bottom: 8px; }
  .mood-row { display: flex; gap: 22px; font-size: 15px; }
  .mood-row span.opt { display: flex; align-items: center; gap: 8px; }
  .write-line { left: 210px; width: 420px; border-bottom: 1.5px solid var(--teal); }
  .supply { font-size: 15px; line-height: 28px; }
  .footer-wave { left: 0; bottom: 0; width: 760px; height: 200px; }
</style>
</head>
<body>
<main class="log-page">
  <div class="abs hero-photo" role="img" aria-label="Photograph of a baby crawling on a soft white blanket"></div>

  <header class="abs brand">
    <span class="brand-dot"></span>
    <span class="brand-name">Quill Harbor Pages</span>
  </header>

  <div class="abs field" style="left:40px; top:228px;">Name: <span class="rule" style="width:300px"></span></div>
  <div class="abs field" style="left:410px; top:228px;">Date: <span class="rule" style="width:180px"></span></div>

  <div class="abs section-title" style="left:40px; top:262px;">Nap Time</div>
  <table class="abs grid" style="left:40px; top:286px;">
    <tr><td class="head">Time</td><td></td><td></td><td></td><td></td></tr>
    <tr><td class="head">How Long</td><td></td><td></td><td></td><td></td></tr>
  </table>

  <div class="abs section-title" style="left:400px; top:262px;">Feeding</div>
  <table class="abs grid" style="left:400px; top:286px;">
    <tr><td class="head">Name</td><td></td><td></td><td></td><td></td></tr>
    <tr><td class="head">What</td><td></td><td></td><td></td><td></td></tr>
  </table>

  <div class="abs section-title" style="left:40px; top:365px;">Diapers</div>
  <div class="abs label" style="left:40px; top:398px; font-size:14px;">Time</div>
  <div class="abs label" style="left:105px; top:398px; font-size:14px;">Wet</div>
  <div class="abs label" style="left:145px; top:398px; font-size:14px;">BM</div>
  <div class="abs" style="left:36px; top:420px;">
    <div class="diaper-row"><span class="rule"></span><span class="box"></span><span class="box"></span></div>
    <div class="diaper-row"><span class="rule"></span><span class="box"></span><span class="box"></span></div>
    <div class="diaper-row"><span class="rule"></span><span class="box"></span><span class="box"></span></div>
    <div class="diaper-row"><span class="rule"></span><span class="box"></span><span class="box"></span></div>
    <div class="diaper-row"><span class="rule"></span><span class="box"></span><span class="box"></span></div>
    <div class="diaper-row"><span class="rule"></span><span class="box"></span><span class="box"></span></div>
    <div class="diaper-row"><span class="rule"></span><span class="box"></span><span class="box"></span></div>
  </div>

  <div class="abs section-title" style="left:215px; top:365px;">Mood</div>
  <div class="abs mood-row" style="left:215px; top:405px;">
    <span class="opt">Happy <span class="box"></span></span>
    <span class="opt">Sad <span class="box"></span></span>
    <span class="opt">Unsettled <span class="box"></span></span>
    <span class="opt">Energetic <span class="box"></span></span>
  </div>
  <div class="abs mood-row" style="left:215px; top:455px;">
    <span class="opt">Tired <span class="box"></span></span>
    <span class="opt">Chatty <span class="box"></span></span>
    <span class="opt">Quiet <span class="box"></span></span>
  </div>

  <div class="abs section-title" style="left:210px; top:515px;">Today's Activities</div>
  <div class="abs write-line" style="top:565px;"></div>
  <div class="abs write-line" style="top:600px;"></div>
  <div class="abs write-line" style="top:635px;"></div>
  <div class="abs write-line" style="top:670px;"></div>
  <div class="abs write-line" style="top:705px;"></div>

  <div class="abs section-title" style="left:40px; top:738px;">Supplies Needed Soon</div>
  <div class="abs supply" style="left:40px; top:765px;">
    <div><span class="ring"></span>Diapers</div>
    <div><span class="ring"></span>Diaper Cream</div>
    <div><span class="ring"></span>Other:</div>
  </div>
  <div class="abs supply" style="left:260px; top:780px;">
    <div><span class="ring"></span>Milk/Formula</div>
    <div><span class="ring"></span>Cereal</div>
  </div>
  <div class="abs supply" style="left:470px; top:795px;">
    <div><span class="ring"></span>Wet Wipes</div>
    <div><span class="ring"></span>Baby Food</div>
  </div>

  <div class="abs section-title" style="left:40px; top:858px;">Special Notes</div>

  <svg class="abs footer-wave" viewBox="0 0 760 200" preserveAspectRatio="none" aria-hidden="true">
    <path d="M0 20 Q 380 260 760 110 L760 200 L0 200 Z" fill="var(--teal-deep)"/>
    <path d="M0 20 Q 380 260 760 110" fill="none" stroke="var(--teal-light)" stroke-width="6"/>
  </svg>
</main>
</body>
</html>
```